Natural Cosmetics need a Packaging Design

We need a PACKAGING design for labels on hand/body wash bottles and soap paper boxes.
We target at high end markets.
We expect a contemporary and trendy design.
We don't need a separate logo. The brand name "Va Mirel" acts as the logo.
We want a modern and classic font for "Va Mirel".
Please see attached pictures for packaging samples.

Industry/Entity Type

Cosmetics

Requirements
Should not have
• a separate logo from the brand name

```html
<!DOCTYPE html>
<html lang="en">
<head>
<meta charset="utf-8">
<title>Va Mirel — Packaging Labels</title>
<link href="https://fonts.googleapis.com/css2?family=Raleway:wght@300;400&display=swap" rel="stylesheet">
<style>
  :root {
    --backdrop: #afc0d1;
    --label-white: #f7f7f8;
    --brand-purple: #7a2a8c;
    --band-purple: #7b2f8e;
    --band-blue: #2f8fd6;
    --wave-violet: #8a4fd6;
    --wave-lilac: #c9b3e6;
    --ink-grey: #555a60;
  }
  * { box-sizing: border-box; margin: 0; padding: 0; }
  html, body { width: 1200px; height: 1200px; overflow: hidden; }
  body {
    background: var(--backdrop);
    font-family: "Raleway", sans-serif;
    position: relative;
  }
  .label {
    position: absolute;
    background: var(--label-white);
    border-radius: 6px;
    box-shadow: 0 8px 24px rgba(40, 60, 90, 0.15);
    overflow: hidden;
    text-align: center;
  }
  .label--body { left: 120px; top: 300px; width: 280px; height: 500px; }
  .label--hand { left: 460px; top: 420px; width: 300px; height: 380px; }
  .label--soap { left: 820px; top: 520px; width: 280px; height: 280px; }

  .brand-name {
    position: absolute;
    left: 0; right: 0;
    font-family: "Raleway", sans-serif;
    font-weight: 400;
    color: var(--brand-purple);
    font-size: 30px;
    letter-spacing: 1px;
  }
  .label--body .brand-name { top: 70px; }
  .label--hand .brand-name { top: 60px; }
  .label--soap .brand-name { top: 36px; font-size: 28px; }

  .wave-art { position: absolute; left: 0; width: 100%; }
  .label--body .wave-art { top: 140px; height: 230px; }
  .label--hand .wave-art { top: 130px; height: 150px; }
  .label--soap .wave-art { top: 70px; height: 200px; }

  .product-line {
    position: absolute; left: 0; right: 0;
    font-weight: 300; color: var(--ink-grey);
  }
  .product-band {
    display: inline-block;
    color: #fff;
    font-weight: 300;
    padding: 2px 12px;
    line-height: 1.15;
  }
  .label--body .product-line--name { top: 372px; font-size: 26px; }
  .label--body .product-band { background: var(--band-blue); font-size: 20px; }
  .label--body .product-line--band { top: 404px; }

  .label--hand .product-line--name { top: 218px; font-size: 30px; color: #444; }
  .label--hand .product-band { background: var(--band-purple); font-size: 28px; }
  .label--hand .product-line--band { top: 254px; }
  .label--hand .product-line--note { top: 298px; font-size: 11px; letter-spacing: 0.5px; }

  .volume { position: absolute; left: 0; right: 0; font-size: 12px; font-weight: 300; color: var(--ink-grey); }
  .label--body .volume { bottom: 30px; }
  .label--hand .volume { bottom: 26px; }

  .label--soap .product-line--band { top: 126px; text-align: left; padding-left: 30px; }
  .label--soap .product-band {
    background: linear-gradient(90deg, var(--band-purple), #9a55b8);
    font-size: 28px; padding: 2px 14px;
  }
</style>
</head>
<body>
  <section class="label label--body">
    <div class="brand-name">Va Mirel</div>
    <svg class="wave-art" viewBox="0 0 280 230" preserveAspectRatio="none" role="img" aria-label="Flowing violet smoke waves">
      <defs>
        <linearGradient id="waveBody" x1="0" y1="1" x2="1" y2="0">
          <stop offset="0" stop-color="var(--wave-lilac)" stop-opacity="0.3"/>
          <stop offset="0.5" stop-color="var(--wave-violet)" stop-opacity="0.55"/>
          <stop offset="1" stop-color="var(--wave-lilac)" stop-opacity="0.2"/>
        </linearGradient>
      </defs>
      <path d="M0 120 C80 40 180 20 280 10 L280 150 C190 160 90 200 0 230 Z" fill="url(#waveBody)"/>
    </svg>
    <div class="product-line product-line--name">body</div>
    <div class="product-line product-line--band"><span class="product-band">WASH</span></div>
    <div class="volume">7.5fl.Oz/221ml</div>
  </section>

  <section class="label label--hand">
    <div class="brand-name">Va Mirel</div>
    <svg class="wave-art" viewBox="0 0 300 150" preserveAspectRatio="none" role="img" aria-label="Flowing violet smoke waves">
      <defs>
        <linearGradient id="waveHand" x1="0" y1="1" x2="1" y2="0">
          <stop offset="0" stop-color="var(--wave-violet)" stop-opacity="0.45"/>
          <stop offset="0.6" stop-color="var(--wave-lilac)" stop-opacity="0.35"/>
          <stop offset="1" stop-color="var(--wave-lilac)" stop-opacity="0.1"/>
        </linearGradient>
      </defs>
      <path d="M0 90 C90 40 200 30 300 50 L300 90 C200 80 90 110 0 150 Z" fill="url(#waveHand)"/>
    </svg>
    <div class="product-line product-line--name">hand</div>
    <div class="product-line product-line--band"><span class="product-band">WASH</span></div>
    <div class="product-line product-line--note">SENSITIVE SKIN</div>
    <div class="volume">7.5fl.Oz/221ml</div>
  </section>

  <section class="label label--soap">
    <div class="brand-name">Va Mirel</div>
    <svg class="wave-art" viewBox="0 0 280 200" preserveAspectRatio="none" role="img" aria-label="Flowing violet smoke waves">
      <defs>
        <linearGradient id="waveSoap" x1="0" y1="1" x2="1" y2="0">
          <stop offset="0" stop-color="var(--wave-violet)" stop-opacity="0.75"/>
          <stop offset="0.6" stop-color="var(--wave-violet)" stop-opacity="0.45"/>
          <stop offset="1" stop-color="var(--wave-lilac)" stop-opacity="0.2"/>
        </linearGradient>
      </defs>
      <path d="M0 200 C80 130 180 60 280 0 L280 100 C190 120 100 170 20 200 Z" fill="url(#waveSoap)"/>
    </svg>
    <div class="product-line product-line--band"><span class="product-band">SOAP</span></div>
  </section>
</body>
</html>
```